Medigap Insurance Interactive website

We are looking at redesigning our website for a more up to date and responsive look and feel. We will code this site using Bootstrap 3 so please research and know how to design for this. Attached is our logo and a wireframe for the new site.
I look forward to seeing what you guys can do.

Target Market(s)

People elegible for Medigap Insurance in the US

Industry/Entity Type

Insurance

Number of Pages Required

5+ page

Font styles to use
Sans Serif

Requirements
Must have
• Match the logo
• Be Bootstrap 3 compatible design
• Font Awesome Icons

```html
<!DOCTYPE html>
<html lang="en">
<head>
<meta charset="utf-8">
<title>Harborline – Medicare Supplement Insurance</title>
<link href="https://fonts.googleapis.com/css2?family=Bree+Serif&family=Lato:ital,wght@0,400;0,700;1,400&display=swap" rel="stylesheet">
<style>
:root{
  --navy:#0b2d63;
  --red:#c8251c;
  --red-btn:#d42a20;
  --ink:#1c1c1c;
  --muted:#555;
  --page:#f3f3f3;
  --white:#fff;
  --line:#dcdcdc;
}
*{box-sizing:border-box;margin:0;padding:0}
html,body{width:1200px;height:1018px;overflow:hidden}
body{position:relative;background:var(--page);font-family:'Lato',sans-serif;color:var(--ink)}
.topbar{position:absolute;left:0;top:0;width:1200px;height:35px;background:var(--navy)}
.social{position:absolute;left:81px;top:6px;display:flex;gap:7px}
.social span{width:22px;height:22px;border-radius:50%;background:var(--red)}
.phone{position:absolute;right:81px;top:6px;display:flex;align-items:center;gap:8px;color:var(--white);font-size:17px;letter-spacing:.3px}
.phone .dot{width:22px;height:22px;border-radius:50%;background:var(--red);display:flex;align-items:center;justify-content:center}
.header{position:absolute;left:0;top:35px;width:1200px;height:90px;background:#fafafa;border-bottom:1px solid var(--line)}
.brand{position:absolute;left:82px;top:22px;font-family:'Lato',sans-serif;font-weight:700;font-size:34px;color:var(--navy);letter-spacing:1px}
.nav{position:absolute;left:414px;top:39px;display:flex;align-items:center;font-family:'Bree Serif',serif;font-size:15.5px}
.nav a{color:var(--ink);text-decoration:none;padding:0 13px;border-left:1px solid #999;line-height:13px}
.nav a:first-child{border-left:0;padding-left:0}
.nav a.active{color:var(--red);position:relative}
.nav a.active::after{content:"";position:absolute;left:0;right:13px;top:20px;height:3px;background:var(--navy)}
.hero{position:absolute;left:0;top:125px;width:1200px;height:441px;background:linear-gradient(100deg,#c9b5a4 0%,#e0c9b8 30%,#a9b9c6 60%,#7f98ae 100%)}
.hero-photo{position:absolute;inset:0}
.video{position:absolute;left:745px;top:47px;width:373px;height:304px;border:1px solid var(--navy);background:#1b1b1b}
.video-frame{position:absolute;left:0;top:0;width:371px;height:271px;background:linear-gradient(120deg,#d9dde2,#a6b0ba 55%,#6d7885)}
.video-play{position:absolute;left:153px;top:111px;width:70px;height:49px;border-radius:10px;background:rgba(60,60,60,.75)}
.video-bar{position:absolute;left:0;bottom:0;width:371px;height:32px;background:#111;display:flex;align-items:center;color:var(--white);font-size:13px}
.video-bar .time{margin:0 8px}
.track{width:174px;height:8px;border-radius:4px;background:#3a3a3a;position:relative}
.track::after{content:"";position:absolute;left:0;top:0;width:108px;height:8px;border-radius:4px;background:#555}
.track .knob{position:absolute;left:103px;top:-1px;width:10px;height:10px;border-radius:50%;background:#888;z-index:1}
.caption{position:absolute;left:0;top:371px;width:1200px;height:70px;background:rgba(80,80,80,.55)}
.caption h1{position:absolute;left:132px;top:17px;font-family:'Bree Serif',serif;font-weight:400;font-size:31.5px;color:var(--white);white-space:nowrap}
.btn-quote{position:absolute;left:937px;top:15px;width:130px;height:40px;background:var(--red-btn);color:var(--white);font-size:17px;display:flex;align-items:center;justify-content:center;border-radius:2px}
.features{position:absolute;left:0;top:566px;width:1200px;height:127px;background:linear-gradient(#f0f0f0,#fafafa);border-bottom:1px solid var(--line)}
.feature{position:absolute;top:34px;display:flex;align-items:center;gap:11px;font-family:'Bree Serif',serif;font-size:18px;color:var(--navy)}
.feature .icon{width:60px;height:60px;border-radius:50%;background:var(--navy);display:flex;align-items:center;justify-content:center}
.chev{position:absolute;top:12px}
.col{position:absolute;top:730px}
.col h2{font-family:'Bree Serif',serif;font-weight:400;font-size:20px;color:var(--navy);display:flex;gap:5px}
.col h2 span{padding-bottom:2px;border-bottom:2px solid var(--navy)}
.col h2 .accent{color:var(--red);border-color:var(--red)}
.about{left:79px;width:325px}
.about p{margin-top:14px;margin-left:5px;font-size:14px;line-height:18.6px}
.testimonials{left:453px;width:292px}
.quote{margin-top:15px;background:var(--white);border-radius:8px;padding:12px 16px 12px 17px;font-style:italic;font-size:13px;line-height:20px;color:var(--muted);position:relative;box-shadow:0 1px 2px rgba(0,0,0,.08)}
.quote::after{content:"";position:absolute;left:160px;bottom:-12px;border-left:12px solid var(--white);border-bottom:12px solid transparent}
.quote .mark{font-family:'Bree Serif',serif;font-size:30px;color:#bbb;line-height:0;vertical-align:-10px;margin-right:4px}
.author{display:flex;align-items:center;gap:20px;margin-top:-12px;margin-left:15px;font-weight:700;font-size:14px;color:#333}
.avatar{width:74px;height:74px;border-radius:50%;border:4px solid var(--white);box-shadow:0 1px 3px rgba(0,0,0,.3);background:linear-gradient(#5b7e58,#c99b80)}
.updates{left:798px;width:322px}
.updates p{margin-top:14px;font-size:14.5px;line-height:19px}
.email{margin-top:12px;width:322px;height:35px;border:1px solid #ccc;border-radius:3px;background:#f7f7f7;font-size:14.5px;color:#777;padding:8px 10px}
.btn-signin{margin-top:16px;width:74px;height:31px;background:var(--navy);color:var(--white);font-size:14px;display:flex;align-items:center;justify-content:center;border-radius:2px}
.divider{position:absolute;top:725px;width:1px;height:225px;background:#e4e4e4}
.footer{position:absolute;left:0;top:972px;width:1200px;height:46px;background:var(--navy);color:var(--white);font-size:14px}
.footer .copy{position:absolute;left:79px;top:15px}
.footer .links{position:absolute;right:80px;top:15px}
.footer .links span{margin:0 5px}
</style>
</head>
<body>
<div class="topbar">
  <div class="social"><span></span><span></span><span></span><span></span></div>
  <div class="phone"><span class="dot"><svg width="12" height="12" viewBox="0 0 24 24"><path fill="#fff" d="M6.6 10.8c1.4 2.8 3.8 5.1 6.6 6.6l2.2-2.2c.3-.3.7-.4 1-.2 1.1.4 2.3.6 3.6.6.6 0 1 .4 1 1V20c0 .6-.4 1-1 1C10.6 21 3 13.4 3 4c0-.6.4-1 1-1h3.5c.6 0 1 .4 1 1 0 1.3.2 2.5.6 3.6.1.3 0 .7-.2 1z"/></svg></span>(888) 555-0142</div>
</div>

<div class="header">
  <div class="brand">HARBORLINE</div>
  <nav class="nav">
    <a class="active">Medicare Supplement</a><a>Part D</a><a>How To Decide</a><a>Learn Online</a><a>Why Harborline</a><a>Buy Now</a>
  </nav>
</div>

<section class="hero">
  <div class="hero-photo" role="img" aria-label="Photo of a smiling three-generation family on a beach"></div>
  <div class="video">
    <div class="video-frame" role="img" aria-label="Video still of an advisor reviewing documents with a couple"></div>
    <div class="video-play"><svg width="70" height="49" viewBox="0 0 70 49"><path d="M30 15l16 9.5L30 34z" fill="#fff"/></svg></div>
    <div class="video-bar">
      <svg width="42" height="32" viewBox="0 0 42 32"><path d="M16 10l11 6-11 6z" fill="#fff"/></svg>
      <span class="time">04:59</span>
      <div class="track"><span class="knob"></span></div>
      <span class="time">10:35</span>
      <svg width="22" height="20" viewBox="0 0 22 20"><path d="M2 7h4l5-4v14l-5-4H2z" fill="#fff"/><path d="M14 6a5 5 0 010 8M16 3a9 9 0 010 14" stroke="#fff" stroke-width="1.5" fill="none"/></svg>
      <svg width="36" height="20" viewBox="0 0 36 20"><path d="M10 2h6v2h-3l4 4-1.5 1.5-4-4v3h-2zM26 18h-6v-2h3l-4-4 1.5-1.5 4 4v-3h2z" fill="#fff"/></svg>
    </div>
  </div>
  <div class="caption">
    <h1>It's Time To Take Action And Protect What Matters Most</h1>
    <div class="btn-quote">GET QUOTE</div>
  </div>
</section>

<section class="features">
  <div class="feature" style="left:81px"><span class="icon"><svg width="30" height="30" viewBox="0 0 30 30" fill="none" stroke="#fff" stroke-width="3"><path d="M9 26V6M4 11l5-5 5 5M21 4v20M16 19l5 5 5-5"/></svg></span>Compare Rates</div>
  <svg class="chev" style="left:308px" width="46" height="104" viewBox="0 0 46 104"><path d="M2 2l42 50L2 102" fill="none" stroke="#e2e2e2" stroke-width="4"/></svg>
  <div class="feature" style="left:388px"><span class="icon"><svg width="34" height="30" viewBox="0 0 34 30"><text x="17" y="14" font-family="Lato,sans-serif" font-size="16" font-weight="700" fill="#fff" text-anchor="middle">$</text><path d="M3 20h8l5 2h8l6-4v3l-7 5H14l-6-2H3z" fill="#fff"/></svg></span>Buy Now</div>
  <svg class="chev" style="left:563px" width="46" height="104" viewBox="0 0 46 104"><path d="M2 2l42 50L2 102" fill="none" stroke="#e2e2e2" stroke-width="4"/></svg>
  <div class="feature" style="left:642px"><span class="icon"><svg width="34" height="24" viewBox="0 0 34 24"><rect x="6" y="3" width="22" height="14" rx="1" fill="#fff"/><path d="M2 19h30v2H2z" fill="#fff"/><ellipse cx="17" cy="10" rx="6" ry="3.5" fill="#0b2d63"/><circle cx="17" cy="10" r="2" fill="#fff"/></svg></span>Learn Online</div>
  <svg class="chev" style="left:846px" width="46" height="104" viewBox="0 0 46 104"><path d="M2 2l42 50L2 102" fill="none" stroke="#e2e2e2" stroke-width="4"/></svg>
  <div class="feature" style="left:925px"><span class="icon"><svg width="32" height="32" viewBox="0 0 32 32" fill="none" stroke="#fff" stroke-width="2.5"><circle cx="16" cy="17" r="8"/><path d="M5 17v-3a11 11 0 0122 0v3"/><rect x="3" y="14" width="4" height="7" fill="#fff"/><rect x="25" y="14" width="4" height="7" fill="#fff"/></svg></span>Get Expert Help</div>
</section>

<div class="col about">
  <h2><span>About</span><span class="accent">Harborline</span></h2>
  <p>Lorem ipsum dolor sit amet, consectetur adipiscing elit. Sed vitae magna tellus. Aenean ante nunc, semper nec cursus non, rutrum ac eros. Vestibulum mattis justo ac dui bibendum consequat a ac ipsum. Praesent a arcu venenatis, auctor velit eu, suscipit libero. Quisque convallis, leo ac pharetra sagittis, ipsum arcu auctor urna, sit amet cursus risus augue in eros sit amet cursus.</p>
</div>
<div class="divider" style="left:427px"></div>
<div class="col testimonials">
  <h2><span>What People</span><span class="accent">Are Saying</span></h2>
  <div class="quote"><span class="mark">“</span>Lorem ipsum dolor sit amet conetuge sed diay nibhdl tincidunt ut laoreet dolore magam er vol wisi enim ad minim vni quis nostrud exerci tationorem ipsum...</div>
  <div class="author"><div class="avatar" role="img" aria-label="Portrait of a satisfied customer"></div>Mr.Owen Hartley</div>
</div>
<div class="divider" style="left:770px"></div>
<div class="col updates">
  <h2><span>Monthly</span><span class="accent">Updates</span></h2>
  <p>Enter Your Email for Customized Monthly Rate Update and More..</p>
  <div class="email">Enter Email Id</div>
  <div class="btn-signin">Sign In</div>
</div>

<footer class="footer">
  <div class="copy">Copyright © 2016 HARBORLINE. All Rights Reserved.</div>
  <div class="links">Sitemap<span>|</span>Buy Now<span>|</span>Blog<span>|</span>Login</div>
</footer>
</body>
</html>
```